Halcyon Motion a Centre Pty Ltd

Business card is to promote and represent our new business. It's situated in
48 Wren Parade
Brookvale 2100 Sydney
Our clinic is all about getting people back to great health giving them back their lifestyle in half the usual time it takes to get results elsewhere , we do this through innovative therapies with latest state of the art equipment ,skills ,knowledge and experience.
We give them back their pain free healthy lifestyle with lots of energy to love life and perform their best Quickly and effectively .
The final design should communicate
Trust , confidence, results .

Reason: Waiting for some designers to submit work Thanks

Target Market(s)

High end clients that take their health and results seriously ,
High end athletes , as well as general people that want to see results with different
Treatment Methods and approach

Industry/Entity Type

Clinic

Contact Information for Business Card

Halcyon Motion Centre Pty Ltd
48 Wren Parade Brookvale 2100 Sydney
Website www.halcyonmotioncentre.com.au

Font styles to use
Other font styles liked:
• Gothic font medium

Requirements
Must have
• A designe that makes people look twice with a wow factor , a designe that isn't like all the rest .
• Must have the logo in the colours Iv provided in my files
• Must communicate Trust, confidence , results
Nice to have
• 1) The logo raised up or
• 2) Maybe a pop up logo on the card ?
• Or let's be creative and have two cards one on top of the other so the two cards slide .... The front will have the halcyon logo with the address details etc
• The other card with have
• eg your next app .......................................repeating all way down the card
Should not have
• Basic plain looking card that everyone else has

```html
<!DOCTYPE html>
<html lang="en">
<head>
<meta charset="utf-8">
<title>Halcyon Motion Centre – Business Card</title>
<link href="https://fonts.googleapis.com/css2?family=Lato:wght@400;700;900&display=swap" rel="stylesheet">
<style>
  :root {
    --stage: #d9dadb;
    --card-white: #ffffff;
    --card-dark: #1f1f1f;
    --green: #2e8b3a;
    --green-light: #6cc04a;
    --green-deep: #1f6e2c;
    --navy: #2c2f7a;
    --text-dark: #2a2a2a;
    --text-light: #f2f2f2;
  }
  * { box-sizing: border-box; margin: 0; padding: 0; }
  html, body { width: 1200px; height: 900px; overflow: hidden; }
  body {
    background: var(--stage);
    font-family: "Lato", Arial, sans-serif;
    position: relative;
  }
  .card {
    position: absolute;
    width: 640px;
    height: 366px;
    border-radius: 4px;
    overflow: hidden;
    box-shadow: 0 6px 18px rgba(0,0,0,.18);
  }

  /* Front */
  .card-front { left: 80px; top: 60px; background: var(--card-white); }
  .brand {
    position: absolute; left: 40px; top: 46px;
    display: flex; align-items: center; gap: 14px;
  }
  .brand-dot {
    width: 46px; height: 46px; border-radius: 50%;
    background: var(--green);
  }
  .brand-name {
    font-weight: 700; font-size: 34px; color: var(--green);
    line-height: 1; letter-spacing: .5px;
  }
  .person { position: absolute; left: 40px; top: 160px; }
  .person-name { font-weight: 900; font-size: 22px; color: var(--green); letter-spacing: .5px; }
  .person-title { font-size: 13px; color: var(--text-dark); margin-top: 4px; letter-spacing: .5px; }
  .contact-list { position: absolute; left: 40px; top: 236px; list-style: none; }
  .contact-list li {
    display: flex; align-items: center; gap: 10px;
    font-size: 15px; color: var(--text-dark); margin-bottom: 6px;
  }
  .contact-list svg { width: 14px; height: 14px; flex: none; }
  .address {
    position: absolute; right: 36px; top: 160px; text-align: right;
    font-size: 14px; line-height: 1.35; color: var(--text-dark);
  }
  .address-org { color: var(--green); }
  .front-band {
    position: absolute; left: 0; right: 0; bottom: 0; height: 16px;
    background: linear-gradient(90deg, var(--green-deep), var(--green) 45%, var(--green-light));
  }
  .front-band::before {
    content: ""; position: absolute; left: 0; right: 0; top: -4px; height: 2px;
    background: var(--green);
  }

  /* Back */
  .card-back { left: 480px; top: 474px; background: var(--card-dark); }
  .back-url {
    position: absolute; right: 36px; top: 70px;
    font-size: 17px; font-weight: 700; color: var(--text-light); letter-spacing: .3px;
  }
  .back-brand {
    position: absolute; left: 48px; bottom: 70px;
    display: flex; align-items: center; gap: 18px;
  }
  .back-brand .brand-dot { width: 64px; height: 64px; background: var(--green-light); }
  .back-brand .brand-name { font-size: 40px; color: var(--green-light); }
</style>
</head>
<body>

<section class="card card-front">
  <div class="brand">
    <span class="brand-dot"></span>
    <span class="brand-name">Halcyon Motion Centre</span>
  </div>

  <div class="person">
    <p class="person-name">MARCUS HALE</p>
    <p class="person-title">M.B.B.S, M.D.</p>
  </div>

  <ul class="contact-list">
    <li>
      <svg viewBox="0 0 16 16"><path fill="#2c5fa8" d="M4 1l2.5 3-1.5 1.5c.8 2 2.5 3.7 4.5 4.5L11 8.5l3 2.5-1.5 3C7 14 2 9 2 2.5z"/></svg>
      02 5550 1842
    </li>
    <li>
      <svg viewBox="0 0 16 16"><rect x="1" y="3" width="14" height="10" rx="1" fill="#2c5fa8"/><path d="M1.5 3.5L8 9l6.5-5.5" fill="none" stroke="#fff" stroke-width="1.2"/></svg>
      yourname@halcyonmotion.com.au
    </li>
    <li>
      <svg viewBox="0 0 16 16"><circle cx="8" cy="8" r="7" fill="#2c8fd0"/><path d="M1 8h14M8 1c-3 3.5-3 10.5 0 14M8 1c3 3.5 3 10.5 0 14" fill="none" stroke="#fff" stroke-width=".9"/></svg>
      www.halcyonmotioncentre.com.au
    </li>
  </ul>

  <address class="address" style="font-style:normal">
    <span class="address-org">Halcyon Motion Centre</span><br>
    48 Wren Parade Brookvale<br>
    2100 Sydney
  </address>

  <div class="front-band"></div>
</section>

<section class="card card-back">
  <p class="back-url">www.halcyonmotion.com.au</p>
  <div class="back-brand">
    <span class="brand-dot"></span>
    <span class="brand-name">Halcyon Motion Centre</span>
  </div>
</section>

</body>
</html>
```